Business Card Design Project

KV Strategy Partners is a management consulting business with C-suite (CEO/CFO etc) target clients. Logo selected is blue with simple/serious typefaces.

Target Market(s)

CEOs and CFOs of large corporates

Industry/Entity Type

Management Consulting

Font styles to use
Serif

Colors
3276b5

Requirements
Must have
• Tag line: Shaping Enduring Partnerships (use different font)
Address: 457 Cedar Brook Lane #03-22 Singapore 519307
Telephone: +65 8372 6094
Email: kvlorne@mailbox47.com

```html
<!DOCTYPE html>
<html lang="en">
<head>
<meta charset="utf-8">
<title>KV Strategy Partners – Business Cards</title>
<link rel="stylesheet" href="https://fonts.googleapis.com/css2?family=Tinos&family=Crimson+Text:ital,wght@1,700&family=Arimo:wght@400;700&display=swap">
<style>
  :root {
    --brand-blue: #3276b5;
    --brand-blue-deep: #1a5f93;
    --brand-blue-light: #2a8ac4;
    --card-white: #f7f7f7;
    --text-grey: #444444;
    --page-bg: #e9e6df;
    --rule-white: rgba(255, 255, 255, 0.9);
  }
  * { box-sizing: border-box; margin: 0; padding: 0; }
  html, body {
    width: 1200px; height: 800px; overflow: hidden;
    background: var(--page-bg);
  }
  .canvas {
    width: 1200px; height: 800px;
    display: flex; align-items: center; justify-content: center; gap: 50px;
  }
  .card {
    position: relative;
    width: 525px; height: 300px;
    border-radius: 3px;
    box-shadow: 0 6px 18px rgba(0, 0, 0, 0.18);
    overflow: hidden;
  }

  /* Front */
  .card--front {
    background: linear-gradient(135deg, var(--brand-blue-light) 0%, var(--brand-blue) 50%, var(--brand-blue-deep) 100%);
  }
  .brand-name {
    position: absolute; left: 0; right: 0;
    text-align: center;
    font-family: "Tinos", serif;
    font-weight: 400;
    letter-spacing: 0.5px;
    white-space: nowrap;
  }
  .card--front .brand-name {
    top: 108px; font-size: 36px; color: #ffffff;
  }
  .tagline-row {
    position: absolute; left: 38px; right: 38px; top: 210px;
    display: flex; align-items: center; gap: 10px;
  }
  .tagline-rule { flex: 1; height: 1px; background: var(--rule-white); }
  .tagline {
    font-family: "Crimson Text", serif;
    font-style: italic; font-weight: 700;
    font-size: 17px; color: #ffffff; white-space: nowrap;
  }

  /* Back */
  .card--back { background: var(--card-white); }
  .card--back .brand-name {
    top: 34px; font-size: 30px; color: var(--brand-blue);
  }
  .divider {
    position: absolute; left: 40px; right: 40px;
    height: 1px; background: var(--brand-blue);
  }
  .divider--top { top: 92px; }
  .divider--bottom { top: 214px; }
  .person-name {
    position: absolute; left: 0; right: 0; top: 118px;
    text-align: center;
    font-family: "Arimo", sans-serif; font-weight: 700;
    font-size: 16px; color: var(--brand-blue);
  }
  .address {
    position: absolute; right: 40px; top: 152px;
    font-family: "Arimo", sans-serif; font-size: 11.5px;
    line-height: 1.55; color: var(--text-grey); font-style: normal;
  }
  .contact-list {
    position: absolute; left: 40px; top: 234px;
    list-style: none;
    font-family: "Arimo", sans-serif; font-size: 11.5px; color: var(--text-grey);
  }
  .contact-item { display: flex; align-items: center; gap: 9px; line-height: 1.7; }
  .contact-icon { width: 11px; height: 11px; fill: var(--brand-blue); }
  .edge-band {
    position: absolute; left: 0; right: 0; bottom: 0; height: 10px;
    background: var(--brand-blue);
  }
</style>
</head>
<body>
<main class="canvas">
  <section class="card card--front" aria-label="Business card front">
    <h1 class="brand-name">KV Strategy Partners</h1>
    <div class="tagline-row">
      <span class="tagline-rule"></span>
      <p class="tagline">Shaping Enduring Partnerships</p>
      <span class="tagline-rule"></span>
    </div>
  </section>

  <section class="card card--back" aria-label="Business card back">
    <h2 class="brand-name">KV Strategy Partners</h2>
    <div class="divider divider--top"></div>
    <p class="person-name">Kai Vern LORNE</p>
    <address class="address">457 Cedar Brook Lane #03-22<br>Singapore 519307</address>
    <div class="divider divider--bottom"></div>
    <ul class="contact-list">
      <li class="contact-item">
        <svg class="contact-icon" viewBox="0 0 24 24" aria-hidden="true"><path d="M6.6 10.8a15.1 15.1 0 0 0 6.6 6.6l2.2-2.2c.3-.3.7-.4 1-.2 1.1.4 2.3.6 3.6.6.6 0 1 .4 1 1V20c0 .6-.4 1-1 1A17 17 0 0 1 3 4c0-.6.4-1 1-1h3.5c.6 0 1 .4 1 1 0 1.3.2 2.5.6 3.6.1.3 0 .7-.2 1z"/></svg>
        <span>+65 8372 6094</span>
      </li>
      <li class="contact-item">
        <svg class="contact-icon" viewBox="0 0 24 24" aria-hidden="true"><path d="M2 5h20v14H2z M3.5 6.5 12 13l8.5-6.5" fill="var(--brand-blue)" stroke="#ffffff" stroke-width="1.5"/></svg>
        <span>kvlorne@mailbox47.com</span>
      </li>
    </ul>
    <div class="edge-band"></div>
  </section>
</main>
</body>
</html>
```